Postcard for manufacturing company

We make stainless steel essential oil extraction equipment for unique businesses in Washington and Oregon (USA). We are seeking a design for a mailer that will serve as our first contact with potential customers who operate businesses that require this type of equipment. We'd like a large form postcard that integrates the attached photo, along with a few key features. The back should be generic post card format and allow us to add our own sales pitch.
Sales text for front: "State Approved Cannabis Extraction Technology" "Safe - Affordable - Custom" "Specializing in Full Service Solutions" "Free Consultation" "1 855 730 DUNE (3863)"

```html
<!DOCTYPE html>
<html lang="en">
<head>
<meta charset="utf-8">
<title>State Approved Cannabis Extraction Technology – Postcard</title>
<link rel="stylesheet" href="https://fonts.googleapis.com/css2?family=Open+Sans:wght@300;400;600;700&display=swap">
<style>
  :root {
    --ink-black: #050505;
    --steel-light: #c9cacc;
    --steel-mid: #9a9b9e;
    --steel-dark: #4a4b4e;
    --text-white: #ffffff;
    --text-soft: #d9d9d9;
    --text-dark: #1a1a1a;
    --photo-steel: #b8bbbd;
    --photo-shadow: #6f7275;
  }
  * { margin: 0; padding: 0; box-sizing: border-box; }
  html, body {
    width: 837px;
    height: 1200px;
    overflow: hidden;
    background: #ffffff;
  }
  .postcard {
    position: relative;
    width: 837px;
    height: 1200px;
    overflow: hidden;
    font-family: "Open Sans", Arial, sans-serif;
    background:
      repeating-linear-gradient(90deg, rgba(255,255,255,0.05) 0 2px, rgba(0,0,0,0.04) 2px 5px),
      linear-gradient(180deg, var(--steel-light) 0%, var(--steel-mid) 45%, var(--steel-dark) 100%);
  }
  .header-field {
    position: absolute;
    inset: 0 0 auto 0;
    height: 700px;
  }
  .header-text {
    position: absolute;
    top: 28px;
    left: 0;
    width: 100%;
    text-align: center;
    color: var(--text-white);
  }
  .header-text .kicker {
    font-size: 27px;
    font-weight: 400;
    letter-spacing: 3px;
  }
  .header-text .line-one {
    margin-top: 6px;
    font-size: 58px;
    font-weight: 300;
    letter-spacing: 1px;
    line-height: 1.05;
  }
  .header-text .line-two {
    font-size: 96px;
    font-weight: 300;
    letter-spacing: 3px;
    line-height: 1.05;
  }
  .product-photo {
    position: absolute;
    left: 173px;
    top: 245px;
    width: 491px;
    height: 392px;
    border: 4px solid #ffffff;
    background: radial-gradient(ellipse at 45% 40%, #eef0f1 0%, var(--photo-steel) 55%, var(--photo-shadow) 100%);
  }
  .feature-line {
    position: absolute;
    top: 728px;
    width: 100%;
    text-align: center;
    font-size: 42px;
    font-weight: 400;
    color: var(--text-dark);
  }
  .brand-mark {
    position: absolute;
    top: 830px;
    left: 0;
    width: 100%;
    display: flex;
    justify-content: center;
    align-items: center;
    gap: 14px;
  }
  .brand-mark .dot {
    width: 34px;
    height: 34px;
    border-radius: 50%;
    background: var(--ink-black);
  }
  .brand-mark .name {
    font-size: 40px;
    font-weight: 700;
    color: var(--ink-black);
  }
  .service-line {
    position: absolute;
    top: 972px;
    width: 100%;
    text-align: center;
    font-size: 35px;
    font-weight: 400;
    color: var(--text-soft);
    letter-spacing: 0.5px;
  }
  .offer-line {
    position: absolute;
    top: 1030px;
    width: 100%;
    text-align: center;
    font-size: 64px;
    font-weight: 600;
    color: var(--text-white);
    letter-spacing: 2px;
  }
  .phone-bar {
    position: absolute;
    left: 0;
    bottom: 0;
    width: 100%;
    height: 70px;
    background: var(--ink-black);
    color: var(--text-white);
    text-align: center;
    font-size: 38px;
    font-weight: 600;
    line-height: 70px;
  }
</style>
</head>
<body>
  <div class="postcard">
    <svg class="header-field" viewBox="0 0 837 700" preserveAspectRatio="none" aria-hidden="true">
      <defs>
        <linearGradient id="swoosh" x1="0" y1="0" x2="0" y2="1">
          <stop offset="0" stop-color="#ffffff" stop-opacity="0.9"/>
          <stop offset="1" stop-color="#8d8e91" stop-opacity="0"/>
        </linearGradient>
      </defs>
      <path d="M0 0 H837 V600 Q420 690 0 600 Z" fill="#050505"/>
      <path d="M0 600 Q420 690 837 600 V640 Q420 720 0 640 Z" fill="url(#swoosh)"/>
    </svg>

    <header class="header-text">
      <p class="kicker">STATE APPROVED</p>
      <h1>
        <span class="line-one" style="display:block">CANNABIS EXTRACTION</span>
        <span class="line-two" style="display:block">TECHNOLOGY</span>
      </h1>
    </header>

    <div class="product-photo" role="img" aria-label="Photo of stainless steel extraction equipment with pressure gauges and valves"></div>

    <p class="feature-line">Safe • Affordable • Custom</p>

    <div class="brand-mark">
      <span class="dot"></span>
      <span class="name">Ridgeway Extractors</span>
    </div>

    <p class="service-line">Specializing in Full Service Solutions</p>
    <p class="offer-line">FREE CONSULTATION</p>
    <p class="phone-bar">(855) 730-DUNE (3863)</p>
  </div>
</body>
</html>
```